Fiber Optic Internet flyer promotion Winter 2016-2017

I am looking for a marketing flyer that will not be folded, single sided that will advertise a Fiber Optic internet promotion that we are currently running.

The design should be clean, flow well, quickly grab attention, and if a very few short seconds list what the promotion is, and direct them to contact us.

It needs to list a few features of the promotion, but does not need to be in this order and should flow well with the flyer
1.) Fiber Optic Internet
2.) 100 Mbits for $140 /month or 150 Mbits for $190 /month
3.) Free construction cost up to $10,000, limited funds available.
4.) Limited time offer. Must commit before funds run out.

(555) 274-3916, www.kelvoranet.example

Target Market(s)

Small to large business

Industry/Entity Type

Internet Service Provider

Requirements
Must have
• Eye catching appeal. Quickly convey the message of the promotion and our company name and phone number.
Should not have
• Our company is primarily a wireless ISP. This promotion is all about Fiber Optic. I do not want to draw attention to the "wireless" portion of our business with this flyer.

```html
<!DOCTYPE html>
<html lang="en">
<head>
<meta charset="utf-8">
<title>Fiber Optics Internet – Kelvora Networks</title>
<link rel="stylesheet" href="https://fonts.googleapis.com/css2?family=Ubuntu:wght@300;400;700&display=swap">
<style>
  :root {
    --ink-light: #ffffff;
    --photo-dark: #2a2624;
    --photo-mid: #4a4440;
    --photo-warm: #6b5a4c;
    --photo-pale: #8c8580;
    --footer-grey: #9b9b9b;
    --brand-navy: #1f2e6e;
    --contact-ink: #2b2b2b;
  }
  * { box-sizing: border-box; margin: 0; padding: 0; }
  html, body { width: 846px; height: 1200px; overflow: hidden; background: var(--footer-grey); }
  body { font-family: "Ubuntu", Arial, sans-serif; color: var(--ink-light); }

  .flyer { position: relative; width: 846px; height: 1200px; overflow: hidden; }

  .hero-photo {
    position: absolute; left: 0; top: 0; width: 846px; height: 1038px;
    background:
      radial-gradient(ellipse at 70% 30%, var(--photo-pale) 0%, transparent 45%),
      radial-gradient(ellipse at 35% 65%, var(--photo-warm) 0%, transparent 50%),
      linear-gradient(160deg, var(--photo-mid) 0%, var(--photo-dark) 100%);
  }

  .headline {
    position: absolute; left: 18px; top: 18px;
    font-weight: 700; font-size: 116px; line-height: 143px; letter-spacing: 1px;
  }

  .offer { position: absolute; right: 13px; text-align: right; }
  .offer-main { font-weight: 400; font-size: 33px; line-height: 1.3; }
  .offer-note { font-weight: 300; font-size: 21px; line-height: 1.2; }

  .offer-pricing { top: 482px; }
  .offer-pricing .offer-main { font-weight: 500; line-height: 44px; }
  .offer-construction { top: 706px; }
  .offer-deadline { top: 948px; }
  .offer-construction .offer-main, .offer-deadline .offer-main { font-weight: 300; font-size: 34px; }

  .footer {
    position: absolute; left: 0; top: 1038px; width: 846px; height: 162px;
    background: var(--footer-grey); text-align: center;
  }
  .brand-name {
    display: inline-flex; align-items: center; gap: 12px;
    margin-top: 66px;
    font-weight: 700; font-size: 30px; color: var(--brand-navy); letter-spacing: 1px;
  }
  .brand-dot { width: 18px; height: 18px; border-radius: 50%; background: var(--brand-navy); }
  .contact-line {
    position: absolute; left: 0; right: 0; top: 140px;
    font-weight: 400; font-size: 15px; color: var(--contact-ink);
  }
</style>
</head>
<body>
  <main class="flyer">
    <div class="hero-photo" role="img" aria-label="Photo of a person writing notes in a notebook at a wooden desk beside a laptop and coffee mug, darkened"></div>

    <h1 class="headline">Fiber<br>Optics<br>Internet</h1>

    <section class="offer offer-pricing">
      <p class="offer-main">100 Mbits for $140 /month</p>
      <p class="offer-main">150 Mbits for $190 /month</p>
    </section>

    <section class="offer offer-construction">
      <p class="offer-main">Free construction cost up to $10,000</p>
      <p class="offer-note">limited funds available</p>
    </section>

    <section class="offer offer-deadline">
      <p class="offer-main">Limited time offer</p>
      <p class="offer-note">Must commit before funds run out</p>
    </section>

    <footer class="footer">
      <div class="brand-name"><span class="brand-dot"></span>KELVORA NETWORKS</div>
      <p class="contact-line">(555) 274-3916, www.kelvoranet.example</p>
    </footer>
  </main>
</body>
</html>
```